Maple Dawn Confections. We need a website as delcious as our chocolate.

I need a website to promote our humble chocolate business. We our proud of are chocolate because we use only our favorite ingredients. We believe in originality and complete enjoyment of our chocolates. I am looking for a sleek and smooth website. I would like to see typical pages such as contact information and an intro. I would like to have a product page, which can be easily updated with photos of new chocolate. I would also like to see a page where we can educate customers about chocolate. This might be tricky but I would like our customers to leave the site knowing they are getting great chocolate! I have a logo and general color scheme, which I will try to upload somewhere. I looking for an original and exciting website.
Updates

Websites we like:

1. http://www.corvel-amand.example/ (looks really good)

2. http://www.tilvarocacao.example/

uploaded logo !

Target Market(s)

People who enjoy chocolate.

Industry/Entity Type

Business

Requirements
Must have
• User Friendly
Page were pictures of new chocolate can be easily updated.

Nice to have
• Calming and appetizing music
Section where recent tweets can show up on the site.

```html
<!DOCTYPE html>
<html lang="en">
<head>
<meta charset="utf-8">
<title>Maple Dawn Confections – Product Gallery</title>
<link rel="stylesheet" href="https://fonts.googleapis.com/css2?family=Montserrat:wght@400;600;700&family=Source+Sans+3:wght@400;600&display=swap">
<style>
  :root {
    --pink: #f7c4d4;
    --pink-band: #f8c6d6;
    --rose: #c75a80;
    --cocoa-deep: #1f0d07;
    --cocoa: #3a1a0e;
    --cocoa-glow: #5e2c18;
    --caramel: #d9924c;
    --cream: #ffffff;
    --nav-text: #3b1a10;
    --footer-pink: #f3b6c8;
    --footer-text: #e9d6cf;
  }
  * { box-sizing: border-box; margin: 0; padding: 0; }
  html, body { width: 1200px; height: 1080px; overflow: hidden; }
  body {
    position: relative;
    background:
      radial-gradient(ellipse 700px 600px at 420px 560px, var(--cocoa-glow) 0%, rgba(94,44,24,0) 70%),
      radial-gradient(ellipse 500px 400px at 0px 1000px, #5a2816 0%, rgba(90,40,22,0) 70%),
      linear-gradient(135deg, var(--cocoa) 0%, var(--cocoa-deep) 100%);
    font-family: "Source Sans 3", sans-serif;
    color: var(--cream);
  }

  /* Header */
  .site-header { position: absolute; left: 0; top: 0; width: 1200px; height: 200px; }
  .header-band { position: absolute; left: 0; top: 0; }
  .brand {
    position: absolute; left: 42px; top: 52px;
    font-family: "Montserrat", sans-serif; font-weight: 600;
    color: var(--rose); font-size: 34px; line-height: 1.05;
  }
  .main-nav { position: absolute; top: 80px; left: 326px; display: flex; }
  .main-nav a {
    font-family: "Montserrat", sans-serif; font-weight: 700; font-size: 16px;
    letter-spacing: 1.8px; color: var(--nav-text); text-decoration: none;
    text-transform: uppercase; margin-right: 32px;
  }

  /* Gallery */
  .gallery-head { position: absolute; left: 68px; top: 222px; width: 1056px; display: flex; justify-content: space-between; align-items: baseline; }
  .gallery-title { font-family: "Montserrat", sans-serif; font-weight: 400; font-size: 33px; color: var(--caramel); }
  .gallery-lead { font-family: "Montserrat", sans-serif; font-weight: 400; font-size: 23px; color: var(--cream); }

  .product-grid {
    position: absolute; left: 68px; top: 294px;
    display: grid; grid-template-columns: repeat(3, 338px); column-gap: 20px; row-gap: 26px;
  }
  .product-card { text-align: center; }
  .product-photo { width: 338px; height: 196px; }
  .product-name { font-family: "Montserrat", sans-serif; font-weight: 400; font-size: 24px; color: var(--caramel); margin-top: 12px; line-height: 1.2; }
  .product-text { font-size: 15px; line-height: 19px; margin-top: 4px; }
  .details-button {
    display: inline-block; margin-top: 10px; width: 122px; height: 29px; line-height: 29px;
    background: var(--pink); color: var(--nav-text);
    font-family: "Montserrat", sans-serif; font-weight: 600; font-size: 12.5px;
    text-decoration: none; text-transform: uppercase;
  }
  .tone-1 { background: linear-gradient(135deg, #5a1e2a, #8e4a3c 50%, #3c1410); }
  .tone-2 { background: linear-gradient(90deg, #f4eef2 0%, #e9dcea 45%, #6a3a2a 80%, #f2eef2 100%); }
  .tone-3 { background: linear-gradient(160deg, #f3f0f5 0%, #d8c8e4 35%, #7a4430 70%, #5a2a20 100%); }
  .tone-4 { background: linear-gradient(170deg, #efe6ef 0%, #b9a4d0 35%, #8a5838 65%, #5a3420 100%); }
  .tone-5 { background: linear-gradient(120deg, #f6f1f3 0%, #ebe2ea 35%, #7a4a34 65%, #3c2030 100%); }
  .tone-6 { background: linear-gradient(90deg, #f4e9f0 0%, #e6c8da 45%, #8a5a44 80%, #ece3ee 100%); }

  /* Footer */
  .site-footer { position: absolute; left: 72px; top: 1018px; width: 1052px; display: flex; justify-content: space-between; align-items: center; }
  .footer-nav { display: flex; }
  .footer-nav a {
    font-family: "Montserrat", sans-serif; font-weight: 700; font-size: 12px; letter-spacing: 1.6px;
    color: var(--footer-pink); text-decoration: none; text-transform: uppercase; margin-right: 22px;
  }
  .footer-nav a:last-child { margin-right: 0; }
  .legal { font-size: 13.5px; color: var(--footer-text); white-space: nowrap; }
  .legal a { color: var(--footer-text); text-decoration: none; }
</style>
</head>
<body>
  <header class="site-header">
    <svg class="header-band" width="1200" height="200" viewBox="0 0 1200 200">
      <defs>
        <clipPath id="waveClip">
          <path d="M0 0 H1200 V150 C1040 142 860 148 640 178 C470 200 260 192 0 156 Z"/>
        </clipPath>
        <linearGradient id="photoTone" x1="0" x2="1" y1="0" y2="0.4">
          <stop offset="0" stop-color="#b4607a"/>
          <stop offset="0.35" stop-color="#8a3e4a"/>
          <stop offset="0.65" stop-color="#7a3a2a"/>
          <stop offset="1" stop-color="#5a2418"/>
        </linearGradient>
        <linearGradient id="photoFade" x1="0" x2="1" y1="0" y2="0">
          <stop offset="0" stop-color="#fff" stop-opacity="0"/>
          <stop offset="0.45" stop-color="#fff" stop-opacity="0.85"/>
          <stop offset="1" stop-color="#fff" stop-opacity="1"/>
        </linearGradient>
        <mask id="photoMask">
          <rect x="800" y="0" width="400" height="200" fill="url(#photoFade)"/>
        </mask>
      </defs>
      <g clip-path="url(#waveClip)">
        <rect x="0" y="0" width="1200" height="200" fill="var(--pink-band)"/>
        <rect x="800" y="0" width="400" height="200" fill="url(#photoTone)" mask="url(#photoMask)" role="img" aria-label="Close-up photo of assorted chocolates in purple paper cups"/>
      </g>
    </svg>
    <div class="brand">Maple Dawn<br>Confections</div>
    <nav class="main-nav">
      <a href="#">Home</a>
      <a href="#">About Maple Dawn</a>
      <a href="#">Products</a>
      <a href="#">Contact Us</a>
    </nav>
  </header>

  <main>
    <div class="gallery-head">
      <h1 class="gallery-title">Product Gallery</h1>
      <p class="gallery-lead">A wide selection and a variety of flavors are available</p>
    </div>

    <section class="product-grid">
      <article class="product-card">
        <div class="product-photo tone-1" role="img" aria-label="Photo of chocolate pralines in purple paper cups"></div>
        <h2 class="product-name">Product Gallery 1</h2>
        <p class="product-text">Lorem ipsum dolor sit amet, consectetuer adipiscing<br>elit, sed diam nonummy nibh euismod tincidunt.</p>
        <a class="details-button" href="#">More Details</a>
      </article>
      <article class="product-card">
        <div class="product-photo tone-2" role="img" aria-label="Photo of a gift bag beside an open box of chocolates"></div>
        <h2 class="product-name">Product Gallery 2</h2>
        <p class="product-text">Lorem ipsum dolor sit amet, consectetuer adipiscing<br>elit, sed diam nonummy nibh euismod tincidunt.</p>
        <a class="details-button" href="#">More Details</a>
      </article>
      <article class="product-card">
        <div class="product-photo tone-3" role="img" aria-label="Photo of an open gift box filled with assorted chocolates"></div>
        <h2 class="product-name">Product Gallery 3</h2>
        <p class="product-text">Lorem ipsum dolor sit amet, consectetuer adipiscing<br>elit, sed diam nonummy nibh euismod tincidunt.</p>
        <a class="details-button" href="#">More Details</a>
      </article>
      <article class="product-card">
        <div class="product-photo tone-4" role="img" aria-label="Photo of decorated chocolates on lilac tissue"></div>
        <h2 class="product-name">Product Gallery 4</h2>
        <p class="product-text">Lorem ipsum dolor sit amet, consectetuer adipiscing<br>elit, sed diam nonummy nibh euismod tincidunt.</p>
        <a class="details-button" href="#">More Details</a>
      </article>
      <article class="product-card">
        <div class="product-photo tone-5" role="img" aria-label="Photo of a box of chocolates being opened"></div>
        <h2 class="product-name">Product Gallery 5</h2>
        <p class="product-text">Lorem ipsum dolor sit amet, consectetuer adipiscing<br>elit, sed diam nonummy nibh euismod tincidunt.</p>
        <a class="details-button" href="#">More Details</a>
      </article>
      <article class="product-card">
        <div class="product-photo tone-6" role="img" aria-label="Photo of pink gift boxes and a box of chocolates"></div>
        <h2 class="product-name">Product Gallery 6</h2>
        <p class="product-text">Lorem ipsum dolor sit amet, consectetuer adipiscing<br>elit, sed diam nonummy nibh euismod tincidunt.</p>
        <a class="details-button" href="#">More Details</a>
      </article>
    </section>
  </main>

  <footer class="site-footer">
    <nav class="footer-nav">
      <a href="#">Home</a>
      <a href="#">About Maple Dawn</a>
      <a href="#">Products</a>
      <a href="#">Contact Us</a>
    </nav>
    <p class="legal">Copyright © Maple Dawn Confections homemade with passion | <a href="#">Privacy Policy</a> | <a href="#">Contact Us</a></p>
  </footer>
</body>
</html>
```